Mossy Den Pet Supply

Thank you for your interest in this design contest. We are always welcome to questions and are looking forward to seeing what you can come up with.

We work on a Bootstrap platform with our custom built CMS. We require all designs to be sized accordingly with the bootstrap grid system found here: http://fernlattice.com/css/#grid

At the start of a competition, we are looking for general Home Page Design concepts and an example product grid page.

Homepage: Slide Show/Featured Products/Specials

example website as a reference:https://www.mintcollarworks.com/

Store Product Grid: Show a grid of product thumbnails. Included elements are thumbnail and price. Also included are filters (sort by, show by grid/list).

No photos at this time but Logo is attached. Looking for good quality photo's around the web. Please read the attached creative brief in depth to get an idea f what the client is looking for. Thanks!

```html
<!DOCTYPE html>
<html lang="en">
<head>
<meta charset="utf-8">
<title>Mossy Den Pet Supply</title>
<link href="https://fonts.googleapis.com/css2?family=Open+Sans:wght@400;600;700&family=Lato:wght@400;700&display=swap" rel="stylesheet">
<style>
:root{
  --green:#8cc540;
  --green-dark:#7fb536;
  --green-light:#a3d45c;
  --text:#333;
  --muted:#555;
  --panel:#f7f7f7;
  --line:#e4e4e4;
  --dark:#3a3a3a;
  --teal:#8ac6c0;
}
*{box-sizing:border-box;margin:0;padding:0}
html,body{width:1200px;height:2166px;overflow:hidden}
body{position:relative;background:#fff;font-family:"Open Sans",Arial,sans-serif;color:var(--text)}
.abs{position:absolute}
.photo{position:absolute}

.topbar{left:0;top:0;width:1200px;height:49px;background:var(--green);color:#fff;font-size:12px;font-weight:600}
.topbar .login{left:172px;top:16px}
.topbar .cart{left:234px;top:16px;display:flex;gap:8px;align-items:center}
.topbar .search{left:1010px;top:14px}

.mainnav{left:0;top:49px;width:1200px;height:107px;background:#fff}
.mainnav ul{list-style:none;position:absolute;right:172px;top:45px;display:flex;gap:33px;font-size:13.5px;color:#444}

.brand{left:172px;top:49px;width:146px;height:165px;background:#fff;z-index:3;box-shadow:0 2px 4px rgba(0,0,0,.12);display:flex;flex-direction:column;align-items:center;justify-content:center;gap:10px;text-align:center}
.brand .mark{width:26px;height:26px;background:var(--green);border-radius:50%}
.brand .name{font-weight:700;font-size:17px;line-height:1.15;color:#222}

.hero{left:0;top:156px;width:1200px;height:494px;
  background:
    radial-gradient(ellipse 300px 200px at 880px 230px,rgba(232,170,90,.85),transparent 70%),
    radial-gradient(ellipse 260px 140px at 780px 470px,rgba(90,55,30,.7),transparent 70%),
    radial-gradient(ellipse 420px 220px at 180px 380px,rgba(214,184,110,.9),transparent 70%),
    radial-gradient(ellipse 380px 160px at 220px 60px,rgba(210,120,50,.8),transparent 70%),
    linear-gradient(120deg,#c9a45c 0%,#c48a48 40%,#a9743d 65%,#5e3f26 100%)}
.caption{left:172px;top:344px;width:413px;height:134px;background:rgba(30,30,30,.78);padding:10px 16px;color:#ddd}
.caption h1{font-weight:600;font-size:42px;color:var(--green);line-height:1.05;letter-spacing:.5px}
.caption p{font-size:10.5px;line-height:1.7;margin-top:8px;text-align:justify}
.dots{left:172px;top:498px;display:flex;gap:6px}
.dots span{width:14px;height:14px;border-radius:50%;border:2px solid #fff;background:#222}
.dots span:first-child{background:var(--green)}

.section-title{font-size:15px;color:#333}
.featured-head{left:172px;top:670px;width:858px;height:36px;border-bottom:1px dashed #cfe3ad}
.arrows{display:flex;gap:6px;position:absolute;right:0;top:0}
.arrows span{width:18px;height:18px;border:1px solid #ccc;border-radius:50%;font-size:10px;line-height:16px;text-align:center;color:#666;background:#fff}

.card{position:absolute;top:726px;width:207px;height:227px;border:1px solid var(--line);background:#fff}
.card .img{position:absolute;left:0;top:0;width:205px;height:188px}
.card .cap{position:absolute;left:14px;top:199px;right:12px;font-size:13px;color:#444;display:flex;justify-content:space-between;align-items:center}

.promo{left:172px;top:986px;width:238px;height:364px;background:var(--green);color:#fff;text-align:center}
.promo h2{font-weight:400;font-size:24px;line-height:1.45;margin-top:22px}
.promo .img{left:10px;top:105px;width:218px;height:130px}
.promo .off{position:absolute;left:0;right:0;top:258px;font-size:22px;font-weight:600}
.promo .btn{position:absolute;left:68px;top:302px;width:102px;height:40px;background:#111;border-radius:3px;font-size:14px;line-height:40px}

.specials{left:410px;top:986px;width:620px;height:364px;background:var(--panel);border:1px solid var(--line);border-left:none}
.specials .head{position:absolute;left:27px;top:18px;right:22px;height:44px;border-bottom:1px solid var(--line);font-family:Lato,sans-serif;font-size:20px;color:#222}
.special{position:absolute;top:80px;width:173px}
.special .img{position:relative;width:173px;height:185px}
.special h3{font-size:11.5px;font-weight:400;color:#222;margin-top:18px;letter-spacing:.2px}
.special p{font-size:10px;line-height:1.9;color:#444;margin-top:8px;text-align:justify}

.story-card{left:172px;top:1379px;width:261px;height:322px;border:1px solid var(--line);background:#fff}
.story-card .img{left:4px;top:4px;width:253px;height:171px}
.story-card h4{position:absolute;left:16px;top:198px;font-weight:400;font-size:14px}
.story-card .stars{position:absolute;right:16px;top:199px;font-size:13px;color:#f0a020;letter-spacing:1px}
.story-card .stars i{color:#ccc;font-style:normal}
.story-card p{position:absolute;left:16px;right:16px;top:232px;font-size:10.5px;line-height:1.72;color:#444;text-align:justify}

.welcome-title{left:462px;top:1372px;width:568px;height:40px;border-bottom:1px dashed #cfe3ad;font-family:Lato,sans-serif;font-weight:400;font-size:21px;color:#222}
.welcome-body{left:462px;top:1430px;width:312px;font-size:10.2px;line-height:1.86;color:#444;text-align:justify}
.welcome-body .lead{text-transform:uppercase;font-size:10.5px;margin-bottom:10px;color:#333}
.welcome-body p+p{margin-top:13px}
.welcome-photo{left:800px;top:1434px;width:230px;height:267px}

.band{left:0;top:1737px;width:1200px;height:94px;background:var(--green-dark)}
.circle{position:absolute;width:58px;height:58px;border-radius:50%;background:#fff;display:flex;align-items:center;justify-content:center}
.band .signup-label{position:absolute;left:251px;top:31px;font-size:20px;color:#fff}
.band .field{position:absolute;left:334px;top:26px;width:180px;height:39px;background:#fff}
.band .go{position:absolute;left:496px;top:22px;width:48px;height:48px;border-radius:50%;background:var(--teal);display:flex;align-items:center;justify-content:center}
.band .divider{position:absolute;left:604px;top:0;width:1px;height:94px;background:rgba(255,255,255,.35)}
.band h5{position:absolute;left:739px;top:11px;font-weight:400;font-size:20px;color:#fff}
.band .ship{position:absolute;left:739px;top:44px;width:292px;font-size:10px;line-height:1.95;color:#eef7df;text-align:justify}

.footer{left:0;top:1831px;width:1200px;height:260px;background:var(--green-light)}
.fcol{position:absolute;top:30px}
.fcol h6{font-size:15px;font-weight:400;color:#222;margin-bottom:20px}
.fcol ul{list-style:none;font-size:10.5px;line-height:20.6px;color:#2a2a2a}
.addr{position:absolute;left:796px;display:flex;gap:14px;font-size:12px;line-height:1.55;color:#222;width:240px}
.addr svg{flex:none}

.bottombar{left:0;top:2091px;width:1200px;height:75px;background:var(--dark);color:#ddd;font-size:10px}
.bottombar .copy{position:absolute;left:173px;top:31px}
.bottombar .social{position:absolute;left:595px;top:26px;display:flex;gap:9px}
.bottombar .social span{width:21px;height:21px;border-radius:50%;background:#fff;display:flex;align-items:center;justify-content:center}
.bottombar .links{position:absolute;left:823px;top:31px;display:flex;gap:8px}
</style>
</head>
<body>

<header>
  <div class="abs topbar">
    <span class="abs login">Login</span>
    <span class="abs cart">
      <svg width="16" height="13" viewBox="0 0 16 13"><path d="M1 1h3l2 8h8l1-6H5" fill="none" stroke="#fff" stroke-width="1.6"/><circle cx="7" cy="11.5" r="1.3" fill="#fff"/><circle cx="13" cy="11.5" r="1.3" fill="#fff"/></svg>
      Shopping Cart
    </span>
    <svg class="abs search" width="20" height="20" viewBox="0 0 20 20"><circle cx="8" cy="8" r="6" fill="none" stroke="#fff" stroke-width="2"/><path d="M12.5 12.5L18 18" stroke="#fff" stroke-width="2.4"/></svg>
  </div>

  <nav class="abs mainnav">
    <ul>
      <li>Home</li><li>Dogs</li><li>Cats</li><li>Our Story</li><li>The Scoop</li><li>Find a Retailer</li><li>Shop</li>
    </ul>
  </nav>

  <div class="abs brand">
    <span class="mark"></span>
    <span class="name">Mossy Den<br>Pet Supply</span>
  </div>
</header>

<section class="abs hero" role="img" aria-label="Golden retriever resting on a tan pet bed"></section>
<div class="abs caption">
  <h1>NEW PETS</h1>
  <p>Praesent vestibulum molestie lacus. Aenean nonummy hendrerit mauris. Phasellus porta. Fusce suscipit varius mi. Cum sociis natoque penatibus et magnis dis parturient montes, nascetur ridiculus mus. Nulla dui. Fusce feugiat</p>
</div>
<div class="abs dots"><span></span><span></span><span></span></div>

<svg width="0" height="0" style="position:absolute">
  <symbol id="basket" viewBox="0 0 16 14"><path d="M4 5l4-4 4 4" fill="none" stroke="#8cc540" stroke-width="1.4"/><path d="M1 5h14l-2 8H3z" fill="#8cc540"/><path d="M5 7v4M8 7v4M11 7v4" stroke="#fff" stroke-width="1"/></symbol>
</svg>

<section>
  <div class="abs featured-head">
    <span class="section-title">Featured Products</span>
    <div class="arrows"><span>&#8249;</span><span>&#8250;</span></div>
  </div>
  <div class="card" style="left:172px"><div class="img" role="img" aria-label="Spaniel puppy in a pink pet bed" style="background:radial-gradient(ellipse 70px 60px at 90px 70px,#7a4a3a,transparent 75%),radial-gradient(ellipse 110px 50px at 100px 160px,#b46a6a,transparent 75%),linear-gradient(180deg,#6c6c6c 0%,#d9d6d6 25%,#e8e4e2 60%,#a8786f)"></div><div class="cap">Dog in comfy bed<svg width="16" height="14"><use href="#basket"/></svg></div></div>
  <div class="card" style="left:389px"><div class="img" role="img" aria-label="Terrier lying on white sheets" style="background:radial-gradient(ellipse 60px 60px at 115px 60px,#a8683a,transparent 75%),radial-gradient(ellipse 80px 70px at 110px 140px,#f6f4f0,transparent 80%),linear-gradient(160deg,#f3f1ee,#ddd6cc 60%,#e9e4dc)"></div><div class="cap">Ketasnasaysas luytasas<svg width="16" height="14"><use href="#basket"/></svg></div></div>
  <div class="card" style="left:606px"><div class="img" role="img" aria-label="Two husky puppies" style="background:radial-gradient(ellipse 50px 45px at 60px 85px,#1e1e1e,transparent 80%),radial-gradient(ellipse 50px 45px at 145px 85px,#1e1e1e,transparent 80%),radial-gradient(ellipse 110px 60px at 102px 150px,#f7f7f7,transparent 80%),linear-gradient(180deg,#f0f0f0,#d9d9d9)"></div><div class="cap">Nulla at tortor quam<svg width="16" height="14"><use href="#basket"/></svg></div></div>
  <div class="card" style="left:823px"><div class="img" role="img" aria-label="Golden retriever on a yellow cushion" style="background:radial-gradient(ellipse 120px 60px at 90px 70px,#c57a3c,transparent 75%),radial-gradient(ellipse 120px 50px at 110px 165px,#c9b45a,transparent 75%),linear-gradient(160deg,#a86a38,#d09a58 50%,#b8a058)"></div><div class="cap">Cras diam mauris<svg width="16" height="14"><use href="#basket"/></svg></div></div>
</section>

<section>
  <div class="abs promo">
    <h2>New Bumper<br>and Pillow Beds</h2>
    <div class="photo img" role="img" aria-label="Beagle sitting in a round brown bumper bed" style="background:radial-gradient(ellipse 60px 28px at 109px 55px,#c9a878,transparent 80%),radial-gradient(ellipse 105px 50px at 109px 70px,#6b4128 0%,#5a3520 80%,transparent 100%)"></div>
    <div class="off">Up to 40% OFF</div>
    <div class="btn">Shop Now</div>
  </div>
  <div class="abs specials">
    <div class="head">Specials<div class="arrows" style="top:4px"><span>&#8249;</span><span>&#8250;</span></div></div>
    <div class="special" style="left:28px"><div class="img" role="img" aria-label="White fluffy dog" style="background:radial-gradient(ellipse 70px 80px at 80px 100px,#fbfaf8,transparent 80%),radial-gradient(ellipse 60px 60px at 160px 40px,#8fae5a,transparent 80%),linear-gradient(150deg,#d88a6a,#ece6e0 50%,#e3ddd6)"></div><h3>PRAESENT VESTIBULU</h3><p>Nullam eget felis id metus luctus semper quis vel nulla.</p></div>
    <div class="special" style="left:225px"><div class="img" role="img" aria-label="Dog with bandana on a yellow floral cushion" style="background:radial-gradient(ellipse 50px 40px at 90px 90px,#f1ede6,transparent 80%),radial-gradient(ellipse 100px 40px at 85px 160px,#c9b53a,transparent 80%),linear-gradient(180deg,#d8cfbc,#8f8a7a 55%,#b9a640)"></div><h3>AENEAN PLACERAT TORTOR</h3><p>Nullam eget felis id metus luctus semper quis vel nulla.</p></div>
    <div class="special" style="left:423px"><div class="img" role="img" aria-label="Small terrier on a round dog bed" style="background:radial-gradient(ellipse 65px 35px at 90px 90px,#f3efe8,transparent 80%),radial-gradient(ellipse 95px 45px at 85px 150px,#b99a78,transparent 85%),linear-gradient(180deg,#c7774a,#b86a40 40%,#8a6a4e)"></div><h3>LOREM IPSUM DOLOR</h3><p>Nullam eget felis id metus luctus semper quis vel nulla.</p></div>
  </div>
</section>

<section>
  <div class="abs story-card">
    <div class="photo img" role="img" aria-label="Labrador puppy on a striped blanket in grass" style="background:radial-gradient(ellipse 80px 60px at 125px 95px,#e8d2a0,transparent 80%),radial-gradient(ellipse 140px 35px at 125px 160px,#d45a4a,transparent 80%),linear-gradient(180deg,#5e9a3a,#8fc05a 50%,#cfc5b0)"></div>
    <h4>Our Story</h4>
    <span class="stars">&#9733;&#9733;&#9733;<i>&#9733;&#9733;</i></span>
    <p>Dolor sit amet, consectetuer adipiscing elit, sed diam nonummy nibh euismod tincidunt ut laoreet dolore magna aliquam erat volutpat. Ut wisi enim ad minim veniam.</p>
  </div>
  <h2 class="abs welcome-title">Welcome To Mossy Den Pet Supply</h2>
  <div class="abs welcome-body">
    <div class="lead">Donec blandit orci id velit cursus varius. Fusce</div>
    <p>Aenean placerat tortor ac dui luctus ut mattis est mollis. Donec blandit orci id velit cursus varius. Fusce quam enim, hendrerit nec ultrices a, vestibulum nec enim. Quisque imperdiet ultricies dolor in convallis. Morbi sed fringilla elit. Duis sagittis lectus in orci volutpat elementum. Cras in purus sem. Curabitur augue velit, mollis in suscipit eleifend, faucibus ac elit. Morbi mattis tristique mi, quis lobortis nulla sollicitudin quis. Cras adipiscing enim neque, ut ultrices risus. Pellentesque auctor felis eu</p>
    <p>Quisque imperdiet ultricies dolor in convallis. Morbi sed fringilla elit. Duis sagittis lectus in orci volutpat elementum. Cras in purus sem. Curabitur augue velit, mollis in suscipit eleifend, faucibus ac elit. Morbi mattis tristique mi, quis lobortis nulla sollicitudin quis.</p>
  </div>
  <div class="photo welcome-photo" role="img" aria-label="Labrador wearing a bandana on a yellow cushion" style="background:radial-gradient(ellipse 80px 110px at 115px 120px,#e9d4ac,transparent 80%),radial-gradient(ellipse 130px 50px at 115px 235px,#c6b22e,transparent 80%),linear-gradient(180deg,#cfc8b8,#9a9486 45%,#b8a63a)"></div>
</section>

<section class="abs band">
  <div class="circle" style="left:173px;top:18px">
    <svg width="26" height="18" viewBox="0 0 26 18"><rect x="1" y="1" width="24" height="16" fill="#222"/><path d="M1 1l12 9 12-9" fill="none" stroke="#fff" stroke-width="1.6"/></svg>
  </div>
  <span class="signup-label">Sign up</span>
  <div class="field"></div>
  <div class="go"><svg width="28" height="28" viewBox="0 0 28 28"><circle cx="14" cy="14" r="12" fill="none" stroke="#fff" stroke-width="1.6"/><path d="M9 14h10M15 10l4 4-4 4" fill="none" stroke="#fff" stroke-width="1.8"/></svg></div>
  <div class="divider"></div>
  <div class="circle" style="left:661px;top:18px">
    <svg width="28" height="20" viewBox="0 0 28 20"><rect x="1" y="2" width="16" height="12" fill="#222"/><path d="M17 6h6l4 4v4H17z" fill="#222"/><circle cx="7" cy="16" r="2.6" fill="#222"/><circle cx="21" cy="16" r="2.6" fill="#222"/></svg>
  </div>
  <h5>Free Shipping</h5>
  <p class="ship">Fernwood Lane specializes in designing and creating high-end designed competition figure skating</p>
</section>

<footer>
  <div class="abs footer">
    <div class="fcol" style="left:173px"><h6>OUR STORY</h6><ul><li>Community</li><li>Eco Certified</li><li>Why Millbrook?</li><li>Hand-crafted in the USA</li><li>Pet Care Green Alliance</li><li>Donations and Sponsorships</li><li>Pure Thread Standard</li></ul></div>
    <div class="fcol" style="left:399px"><h6>CUSTOMER SERVICE</h6><ul><li>Online Shopping</li><li>Orders and Returns</li><li>discount offer</li><li>investor relations</li><li>corporate responsibility</li><li>E-gift Voucher</li><li>Payment</li><li>FAQ</li></ul></div>
    <div class="fcol" style="left:594px"><h6>DOG BEDS &amp; MATS</h6><ul><li>Dog Beds</li><li>Dog Mats</li><li>Replacement Bed Parts</li><li>Dog Apparel</li><li>Cozyloop Sweaters</li><li>TrailZip Track Jacket</li></ul></div>
    <div class="fcol" style="left:788px"><h6>ADDRESS</h6></div>
    <div class="addr" style="top:70px">
      <svg width="14" height="22" viewBox="0 0 14 22"><path d="M7 1a6 6 0 0 1 6 6c0 5-6 14-6 14S1 12 1 7a6 6 0 0 1 6-6z" fill="#222"/><circle cx="7" cy="7" r="2.2" fill="#a3d45c"/></svg>
      <span>Mossy Den Pet Supply 108 Fernwood Lane Inc Batangas, Philippines</span>
    </div>
    <div class="addr" style="top:142px;align-items:center">
      <svg width="14" height="24" viewBox="0 0 14 24"><rect x="1" y="1" width="12" height="22" rx="2" fill="none" stroke="#222" stroke-width="2"/><circle cx="7" cy="19" r="1.3" fill="#222"/></svg>
      <span>Call us: +63(9000)12345</span>
    </div>
    <div class="addr" style="top:196px;align-items:center">
      <svg width="20" height="14" viewBox="0 0 20 14"><rect x="1" y="1" width="18" height="12" fill="#222"/><path d="M1 1l9 7 9-7" fill="none" stroke="#a3d45c" stroke-width="1.4"/></svg>
      <span>info@mossydenpetsupply.com</span>
    </div>
  </div>
  <div class="abs bottombar">
    <span class="copy">Copyright © 2014 mossydenpetsupply.com . All rights reserved.</span>
    <div class="social" aria-label="Share links">
      <span><svg width="11" height="10" viewBox="0 0 12 11"><path d="M6 10.5L1.2 5.8A3 3 0 0 1 6 1.8a3 3 0 0 1 4.8 4z" fill="#3a3a3a"/></svg></span>
      <span><svg width="11" height="11" viewBox="0 0 12 12"><path d="M6 .5l1.6 3.6 3.9.4-2.9 2.6.8 3.9L6 9 2.6 11l.8-3.9L.5 4.5l3.9-.4z" fill="#3a3a3a"/></svg></span>
      <span><svg width="11" height="11" viewBox="0 0 12 12"><circle cx="2.5" cy="6" r="1.8" fill="#3a3a3a"/><circle cx="9.5" cy="2.5" r="1.8" fill="#3a3a3a"/><circle cx="9.5" cy="9.5" r="1.8" fill="#3a3a3a"/><path d="M2.5 6l7-3.5M2.5 6l7 3.5" stroke="#3a3a3a" stroke-width="1.1"/></svg></span>
      <span><svg width="11" height="8" viewBox="0 0 12 9"><rect x=".5" y=".5" width="11" height="8" fill="#3a3a3a"/><path d="M.5 .5l5.5 4 5.5-4" fill="none" stroke="#fff" stroke-width="1"/></svg></span>
    </div>
    <div class="links"><span>Home</span>|<span>About</span>|<span>privacy policy</span>|<span>Contact</span></div>
  </div>
</footer>

</body>
</html>
```